Tri-fold Brochure for Law Firm

Double-sided brochure to be folded into 6 sides tri-fold brochure for an estate planning special for new parents or parents-to-be. Brochure will be placed in classes for new parents/young parents.

Target Market(s)

New Parents Aged 24-34

Industry/Entity Type

Law Firm

Font styles to use
Serif

Requirements
Must have
• The information provided in the word document.
Nice to have
• Highlight the phrase "for New Parents."
• You may use the color scheme from our website:
• http://k47.9dw.sitevaultexample.com/

```html
<!DOCTYPE html>
<html lang="en">
<head>
<meta charset="utf-8">
<title>Estate Planning for New Parents – Tri-fold Inside</title>
<link href="https://fonts.googleapis.com/css2?family=Tinos:ital,wght@0,400;0,700;1,400&display=swap" rel="stylesheet">
<style>
  :root {
    --page-bg: #e4e4e4;
    --paper: #f7f6f3;
    --paper-shade: #ecebe7;
    --band-gold: #e3a92a;
    --accent-gold: #d9a11c;
    --ink: #111111;
    --wood-dark: #5a3a24;
    --wood-mid: #8a5d3b;
    --wood-light: #c9a27a;
  }
  * { margin: 0; padding: 0; box-sizing: border-box; }
  html, body {
    width: 1200px; height: 800px; overflow: hidden;
    background: var(--page-bg);
    font-family: "Tinos", "Times New Roman", serif;
    color: var(--ink);
  }
  .brochure {
    position: absolute; left: 30px; top: 30px;
    width: 1140px; height: 740px;
    display: flex;
    background: var(--paper);
    box-shadow: 0 6px 24px rgba(0,0,0,0.18);
    overflow: hidden;
  }
  .panel {
    position: relative;
    width: 380px; height: 100%;
    padding-top: 38px;
    background: linear-gradient(90deg, var(--paper) 0%, var(--paper) 85%, var(--paper-shade) 100%);
  }
  .panel + .panel { border-left: 1px solid #dcdad5; }
  .band {
    background: var(--band-gold);
    padding: 7px 30px;
    font-weight: 700;
    font-size: 15px;
    letter-spacing: 0.1px;
  }
  .panel-body {
    position: relative; z-index: 2;
    padding: 18px 30px 0;
  }
  .panel-body p {
    font-size: 14.5px;
    line-height: 1.22;
    text-align: justify;
    margin-bottom: 11px;
  }
  .subhead {
    font-size: 19px;
    font-weight: 700;
    line-height: 1.15;
    margin: 14px 0 9px;
  }
  .class-term { font-weight: 700; font-size: 16px; }

  .panel-process .panel-body p {
    font-size: 13.5px;
    line-height: 1.18;
    margin-bottom: 8px;
  }
  .panel-process .subhead { font-size: 18px; margin: 10px 0 7px; }

  .legal-photo {
    position: absolute; left: 0; bottom: 0;
    width: 760px; height: 290px; z-index: 1;
    background:
      linear-gradient(180deg, rgba(247,246,243,1) 0%, rgba(247,246,243,0) 25%),
      linear-gradient(180deg, #e8e2d8 0%, #d9c8ad 45%, var(--wood-light) 62%, var(--wood-mid) 78%, var(--wood-dark) 100%);
  }
  .contact {
    position: relative; z-index: 2;
    padding: 8px 30px 0;
  }
  .contact-title {
    color: var(--accent-gold);
    font-size: 27px;
    font-weight: 700;
    letter-spacing: 1px;
    margin-bottom: 8px;
  }
  .phone {
    display: flex; align-items: center; gap: 12px;
    font-size: 22px; font-weight: 700;
    margin-bottom: 5px;
  }
  .phone svg { width: 22px; height: 22px; flex: none; }
</style>
</head>
<body>
<main class="brochure">

  <section class="panel panel-why">
    <h2 class="band">Why Should Every Parent Have A Will?</h2>
    <div class="panel-body">
      <p>Imagine how many people love your children. Would there be a fight over who would care for your children if you passed away without leaving instructions?</p>
      <p>Naming a guardian in your will helps avoid litigation that would cause additional stress to your children and loved ones. You can also name a back-up in the event that your first choice is unable or unwilling to serve as guardian.</p>
      <h3 class="subhead">Should We Prepare A Will Now If We Plan To Have More Children In The Future?</h3>
      <p>There is no reason to put off drafting a will. A will can be written to treat your children as a <span class="class-term">“class”</span> that would include any future children born to or adopted by you.</p>
    </div>
  </section>

  <section class="panel panel-package">
    <h2 class="band">What does the estate planning package include?</h2>
    <div class="panel-body">
      <p>Our estate planning package includes a will, an advance medical directive, and a power of attorney. A will names a guardian for your children and gives instructions on how to distribute your probate property at death. An advance medical directive, also known as a living will, states directions regarding your healthcare decisions in the event that you can't make those decisions yourself. A power of attorney gives someone the ability to handle your financial affairs during your lifetime.</p>
    </div>
  </section>

  <section class="panel panel-process">
    <h2 class="band">How long will the process take?</h2>
    <div class="panel-body">
      <p>Before our first meeting, you will receive information to help you start thinking about some of the decisions we'll make during the initial consultation which lasts approximately one hour. It takes about 2 to 3 weeks after our initial meeting to draft your documents. You will receive draft copies of your documents to review before coming in for your last appointment to sign the documents in front of witnesses and a notary.</p>
      <h3 class="subhead">What happens if I die in Maryland Without a Will?</h3>
      <p>If you are married and have minor children, your spouse will inherit one half of your intestate property and your children will inherit the rest. If you have children but no spouse, your children will inherit everything.</p>
      <p>For most parents, this plan doesn't make sense. Married people generally want their spouse to inherit all of their estate and unmarried people should have more control over how funds are distributed to their minor children.</p>
      <p>Furthermore, Maryland law doesn't take into account nontraditional families. For example, foster children and stepchildren that are not legally adopted will not automatically inherit a share of your estate.</p>
      <p>You can find the complete laws of intestacy (dying without a will) in the Maryland Code of Estates &amp; Trusts §§ 3-101 to 3-303.</p>
    </div>
    <div class="contact">
      <p class="contact-title">CALL US TODAY</p>
      <p class="phone">
        <svg viewBox="0 0 24 24" aria-hidden="true"><circle cx="12" cy="12" r="10.5" fill="none" stroke="#d9a11c" stroke-width="2"/><path d="M8.6 6.8c.5-.3 1 0 1.2.4l.9 1.9c.2.4.1.8-.2 1.1l-.7.6c.6 1.3 1.6 2.4 2.9 3.1l.6-.7c.3-.3.8-.4 1.1-.2l1.9.9c.5.2.7.8.4 1.2-.7 1.300-2 1.900-3.300 1.400-3-1.200-5.200-3.500-6.300-6.400-.4-1.300.2-2.700 1.500-3.300z" fill="#d9a11c"/></svg>
        410-555-0148
      </p>
      <p class="phone">
        <svg viewBox="0 0 24 24" aria-hidden="true"><circle cx="12" cy="12" r="10.5" fill="none" stroke="#d9a11c" stroke-width="2"/><path d="M8.6 6.8c.5-.3 1 0 1.2.4l.9 1.9c.2.4.1.8-.2 1.1l-.7.6c.6 1.3 1.6 2.4 2.9 3.1l.6-.7c.3-.3.8-.4 1.1-.2l1.9.9c.5.2.7.8.4 1.2-.7 1.300-2 1.900-3.300 1.400-3-1.200-5.200-3.500-6.300-6.400-.4-1.300.2-2.700 1.500-3.300z" fill="#d9a11c"/></svg>
        813-555-0172
      </p>
    </div>
  </section>

  <div class="legal-photo" role="img" aria-label="Photo of a wooden judge's gavel, open law books and brass scales of justice on a wooden desk"></div>

</main>
</body>
</html>
```